Letter head / email signature/ contract document templates

We need a professional email signature and letterhead designed for our established carpentry and maintenance company. Our Logo (attached) was originally designed 6 years ago by design guru and we love it, looking for something to compliment it ( not a home job)

```html
<!DOCTYPE html>
<html lang="en">
<head>
<meta charset="utf-8">
<title>Harbourline Handyworks – Stationery</title>
<link href="https://fonts.googleapis.com/css2?family=Roboto:wght@400;500;700&display=swap" rel="stylesheet">
<style>
:root{
  --red:#d4202c;
  --red-dark:#a9171f;
  --ink:#3a3a3c;
  --grey:#6b6b6d;
  --paper:#ffffff;
  --bg-light:#e6e6e7;
  --bg-mid:#cfcfd0;
  --bg-dark:#bdbdbf;
}
*{box-sizing:border-box;margin:0;padding:0}
html,body{width:1200px;height:3001px;overflow:hidden}
body{font-family:'Roboto',sans-serif;color:var(--ink);background:var(--bg-light);position:relative}
address{font-style:normal}
.scene{position:absolute;left:0;width:1200px}
.scene--letter{top:0;height:786px;background:var(--bg-light)}
.scene--slip{top:786px;height:792px;background:#e3e3e4}
.scene--folder{top:1578px;height:862px;background:radial-gradient(ellipse at 55% 20%,#f1f1f1 0%,var(--bg-mid) 60%,#bfbfc0 100%)}
.scene--card{top:2440px;height:561px;background:var(--bg-dark)}
.sheet{position:absolute;background:var(--paper);box-shadow:0 6px 18px rgba(0,0,0,.12)}
.brand{display:flex;align-items:center;gap:8px;font-weight:700;color:var(--ink);white-space:nowrap}
.brand__mark{width:12px;height:12px;background:var(--red);flex:none}
.footer-band{position:absolute;left:0;right:0;bottom:18px;height:8px;display:flex}
.footer-band__dark{width:9%;background:var(--ink)}
.footer-band__red{flex:1;background:var(--red);margin-left:4px}
.roller{position:absolute;bottom:10px;right:16px;width:22px;height:22px;background:var(--grey);border-radius:3px}
/* letterhead */
.letterhead{left:170px;top:70px;width:420px;height:590px;padding:40px 38px}
.letterhead .brand{font-size:15px}
.letterhead__contact{position:absolute;right:36px;top:36px;font-size:8px;line-height:1.6;text-align:right;color:var(--grey)}
.letter__body{margin-top:100px;font-size:8.5px;line-height:1.7;color:var(--grey);width:300px}
.letter__body p{margin-bottom:10px}
.letter__sign{margin-top:26px;font-size:8.5px;color:var(--grey)}
/* envelope */
.envelope{width:520px;height:250px;overflow:hidden}
.envelope__flap{height:70px;background:var(--red);border-radius:0 0 14px 14px;display:flex;align-items:center;justify-content:center}
.envelope__flap .brand{color:#fff;font-size:13px}
.envelope__flap .brand__mark{background:#fff}
.envelope--one{left:630px;top:400px}
.envelope--two{left:560px;top:90px}
/* compliment slip */
.slip{left:160px;top:250px;width:680px;height:330px;padding:36px 40px}
.slip .brand{font-size:15px}
.slip__address{margin-top:10px;font-size:9px;line-height:1.6;color:var(--grey)}
/* folder */
.folder{position:absolute;left:150px;top:160px;width:920px;height:560px;display:flex;box-shadow:0 24px 40px rgba(0,0,0,.25)}
.folder__back{width:50%;background:linear-gradient(135deg,var(--red-dark),var(--red) 45%,var(--red-dark));position:relative}
.folder__back-info{position:absolute;left:0;right:0;bottom:60px;color:#fff;font-size:11px;line-height:1.55;text-align:center}
.folder__front{width:50%;background:linear-gradient(180deg,#fff,#ececec);position:relative;display:flex;align-items:center;justify-content:center}
.folder__front .brand{font-size:26px;gap:12px}
.folder__front .brand__mark{width:18px;height:18px}
.folder__web{position:absolute;right:60px;bottom:48px;font-size:10px;color:var(--grey)}
.folder__web b{color:var(--red);font-weight:500}
/* business card */
.card{left:252px;top:146px;width:696px;height:258px;padding:46px 50px;box-shadow:4px 6px 10px rgba(0,0,0,.25)}
.card__name{font-size:23px;font-weight:500;color:var(--ink)}
.card__role{font-size:20px;color:var(--red);margin-bottom:22px}
.card__address{font-size:14.5px;line-height:1.3;color:var(--ink);margin-bottom:8px}
.card__line{display:flex;align-items:center;gap:6px;font-size:14.5px;line-height:1.4}
.card__line svg{width:11px;height:11px;fill:var(--red);flex:none}
.card .brand{position:absolute;left:400px;top:84px;font-size:20px}
.card__social{position:absolute;left:430px;top:190px;display:flex;align-items:center;gap:5px;font-size:14px}
.card__social i{width:16px;height:16px;border-radius:50%;background:var(--red);display:block}
.card .footer-band{bottom:0;height:16px}
.card .footer-band__dark{width:7%}
.card .roller{bottom:4px;right:6px;width:30px;height:30px}
</style>
</head>
<body>

<section class="scene scene--letter">
  <article class="sheet letterhead">
    <div class="brand"><span class="brand__mark"></span>Harbourline Handyworks</div>
    <address class="letterhead__contact">48 Ferncliff Road,<br>Westbrook, ON L6T 3K2<br>555.214.7780<br>hello@harbourlinehandyworks.com<br>www.harbourlinehandyworks.com</address>
    <div class="letter__body">
      <p>Dear customer,</p>
      <p>Thank you for choosing our team for your recent repair work. We value your trust and aim to deliver careful, lasting craftsmanship on every job we take on.</p>
      <p>Please find the details of the proposed works and schedule attached. Our carpenters will contact you to confirm access times before starting.</p>
      <p>Should you have any questions, reach out at any time and we will respond promptly.</p>
      <p class="letter__sign">Yours sincerely,</p>
    </div>
    <div class="footer-band"><span class="footer-band__dark"></span><span class="footer-band__red"></span></div>
    <div class="roller" role="img" aria-label="Small paint roller illustration"></div>
  </article>
  <article class="sheet envelope envelope--one">
    <div class="envelope__flap"><div class="brand"><span class="brand__mark"></span>Harbourline Handyworks</div></div>
  </article>
</section>

<section class="scene scene--slip">
  <article class="sheet envelope envelope--two">
    <div class="envelope__flap"><div class="brand"><span class="brand__mark"></span>Harbourline Handyworks</div></div>
  </article>
  <article class="sheet slip">
    <div class="brand"><span class="brand__mark"></span>Harbourline Handyworks</div>
    <address class="slip__address">48 Ferncliff Road,<br>Westbrook, ON L6T 3K2</address>
    <div class="footer-band"><span class="footer-band__dark"></span><span class="footer-band__red"></span></div>
    <div class="roller" role="img" aria-label="Small paint roller illustration"></div>
  </article>
</section>

<section class="scene scene--folder">
  <div class="folder">
    <div class="folder__back">
      <address class="folder__back-info">Harbourline Handyworks<br>48 Ferncliff Road, Westbrook, ON L6T 3K2<br>P : +15552147780 E : hello@harbourlinehandyworks.com<br>www.harbourlinehandyworks.com</address>
    </div>
    <div class="folder__front">
      <div class="brand"><span class="brand__mark"></span>Harbourline Handyworks</div>
      <div class="folder__web">www.<b>harbourlinehandyworks</b>.com</div>
      <div class="footer-band"><span class="footer-band__dark"></span><span class="footer-band__red"></span></div>
      <div class="roller" role="img" aria-label="Small paint roller illustration"></div>
    </div>
  </div>
</section>

<section class="scene scene--card">
  <article class="sheet card">
    <h1 class="card__name">TOMAS REUTER</h1>
    <p class="card__role">Director</p>
    <address class="card__address">48 Ferncliff Road,<br>Westbrook, ON L6T 3K2</address>
    <p class="card__line"><svg viewBox="0 0 12 12"><path d="M2 1h3l1 3-2 1a7 7 0 0 0 3 3l1-2 3 1v3c-6 0-9-3-9-9z"/></svg>555.214.7780</p>
    <p class="card__line"><svg viewBox="0 0 12 12"><rect x="0" y="2" width="12" height="8"/></svg>hello@harbourlinehandyworks.com</p>
    <p class="card__line"><svg viewBox="0 0 12 12"><circle cx="6" cy="6" r="6"/></svg>www.harbourlinehandyworks.com</p>
    <div class="brand"><span class="brand__mark"></span>Harbourline Handyworks</div>
    <div class="card__social"><i></i><i></i><i></i>@harbourlinehandy</div>
    <div class="footer-band"><span class="footer-band__dark"></span><span class="footer-band__red"></span></div>
    <div class="roller" role="img" aria-label="Small paint roller illustration"></div>
  </article>
</section>

</body>
</html>
```